8 x 8 Social Media Design - Boss Program #1

Why be a regular Agent, when you can be a Boss?
HALO PRIMEVIEW HOMES GROUP
We offer Four Levels of Participation
You Increase your Earning Potential at Each Level
Level One - Learn to Earn Additional Income Through....
Mortgage Originations - Dual Licensing / No Additional Work
Real Estate Investing - Invest Jointly with Us
Agent Recruitment - Up to 10% Override
Level Two - Team Leader
Level Three - Minority Halo Franchise Ownership
Level Four - Majority Halo Franchise Ownership
For more information visit us at www.jobsathalopview.com and request a meeting with our Managing Broker, Mr. Gordon Malvery.

```html
<!DOCTYPE html>
<html lang="en">
<head>
<meta charset="utf-8">
<title>Boss Program – Halo Primeview Homes Group</title>
<link href="https://fonts.googleapis.com/css2?family=Bebas+Neue&family=Anton&family=Barlow:wght@400;600;700&display=swap" rel="stylesheet">
<style>
  :root{
    --navy:#032337;
    --teal:#009db3;
    --teal-deep:#00889c;
    --card:#ebebed;
    --ink:#3a3a3c;
    --grey-text:#555;
    --line:#c9c9cc;
    --white:#ffffff;
  }
  *{margin:0;padding:0;box-sizing:border-box}
  html,body{width:1154px;height:1200px;overflow:hidden;background:var(--white)}
  .poster{position:relative;width:1154px;height:1200px;background:var(--white);overflow:hidden;font-family:"Barlow",sans-serif}
  .abs{position:absolute}
  .header{left:0;top:0;width:1154px;height:196px;background:var(--navy)}
  .headline{left:51px;top:36px;font-family:"Bebas Neue",sans-serif;color:var(--white);font-size:60px;line-height:58px;letter-spacing:.5px}
  .header-rule{left:576px;top:36px;width:2px;height:126px;background:#55697a}
  .offer{left:617px;top:38px;font-family:"Bebas Neue",sans-serif;font-size:37px;line-height:40px;color:var(--white)}
  .offer .hl{color:var(--teal)}
  .hero-photo{left:0;top:196px;width:567px;height:553px;background:linear-gradient(135deg,#1b1b1d 0%,#2a2d36 45%,#1d2a4a 70%,#141416 100%)}
  .hero-word{left:6px;top:196px;font-family:"Anton",sans-serif;color:var(--teal);font-size:150px;line-height:150px;letter-spacing:-2px;text-shadow:6px 6px 0 #006f80}
  .band{background:var(--teal)}
  .lines{left:0;top:0}
  .card{background:var(--card);border-radius:24px;box-shadow:0 8px 14px rgba(0,0,0,.18)}
  .level-no{font-family:"Bebas Neue",sans-serif;color:var(--teal);font-size:78px;line-height:70px}
  .level-sub{font-family:"Bebas Neue",sans-serif;color:var(--ink);font-size:28px;line-height:30px;margin-top:18px}
  .perk{margin-top:14px;font-size:14px;line-height:17px;color:var(--grey-text)}
  .perk b{color:var(--teal);font-weight:700;display:block}
  .portrait{background:var(--teal);padding:12px 12px 0}
  .portrait .shot{width:100%;background:linear-gradient(160deg,#5a5f66,#2b2d31)}
  .portrait .name{color:var(--white);font-weight:700;font-size:15px;text-align:center;line-height:32px}
  .brand{left:62px;top:1090px;width:250px;text-align:center}
  .brand-mark{display:inline-block;width:26px;height:26px;border-radius:50%;background:var(--teal);vertical-align:middle;margin-right:8px}
  .brand-name{font-weight:700;font-size:17px;color:var(--navy);vertical-align:middle}
  .contact{left:349px;top:1100px;font-size:17px;line-height:22px;color:var(--grey-text)}
  .contact b{color:var(--teal);display:block;font-weight:700}
</style>
</head>
<body>
<div class="poster">
  <header class="abs header"></header>
  <h1 class="abs headline">WHY BE A REGULAR AGENT,<br>WHEN YOU CAN BE A BOSS?</h1>
  <div class="abs header-rule"></div>
  <p class="abs offer"><span class="hl">WE OFFER</span> FOUR <span class="hl">LEVELS OF PARTICIPATION</span><br><span class="hl">YOU</span> INCREASE <span class="hl">YOUR</span> EARNING POTENTIAL<br><span class="hl">AT EACH LEVEL</span></p>

  <div class="abs band" style="left:842px;top:245px;width:312px;height:127px"></div>
  <div class="abs band" style="left:892px;top:766px;width:262px;height:42px"></div>
  <div class="abs band" style="left:0;top:873px;width:330px;height:89px"></div>

  <div class="abs hero-photo" role="img" aria-label="Smiling agent in a blue checked suit and red tie, leaning on a desk against a dark backdrop"></div>
  <div class="abs hero-word">BE A<br>BOSS</div>

  <svg class="abs lines" width="1154" height="1200" aria-hidden="true">
    <g stroke="var(--line)" stroke-width="2" fill="none">
      <path d="M816 150 V210 H1118"/>
      <path d="M700 150 V210"/>
      <path d="M1118 210 V272 H995 V318 H1088 V398 H1154"/>
      <path d="M950 690 V742 H1077 V820 H1154"/>
      <path d="M406 838 H330 M406 838 V920"/>
      <path d="M659 1015 V1089 H1000 V1172 H1154"/>
    </g>
    <g fill="var(--line)">
      <circle cx="980" cy="213" r="8"/><circle cx="1118" cy="213" r="8"/>
      <circle cx="1118" cy="272" r="5"/><circle cx="995" cy="274" r="5"/><circle cx="995" cy="316" r="5"/>
      <circle cx="1088" cy="398" r="5"/><circle cx="1077" cy="742" r="5"/>
      <circle cx="406" cy="838" r="5"/><circle cx="406" cy="920" r="5"/>
      <circle cx="659" cy="1089" r="5"/><circle cx="1000" cy="1089" r="5"/><circle cx="1000" cy="1172" r="5"/>
    </g>
  </svg>

  <section class="abs card" style="left:474px;top:214px;width:367px;height:378px;padding:42px 0 0 56px">
    <div class="level-no">01 LEVEL</div>
    <div class="level-sub">LEARN TO EARN<br>ADDITIONAL INCOME THROUGH</div>
    <p class="perk"><b>· Mortgage Originations</b>Dual Licensing / No Additional Work</p>
    <p class="perk"><b>· Real Estate Investing</b>Invest Jointly with Us</p>
    <p class="perk"><b>· Agent Recruitment</b>Up to 10% Override</p>
  </section>

  <section class="abs card" style="left:872px;top:423px;width:253px;height:264px;padding:60px 0 0 20px">
    <div class="level-no">04 LEVEL</div>
    <div class="level-sub" style="margin-top:8px">MAJORITY HALO<br>FRANCHISE OWNERSHIP</div>
  </section>

  <section class="abs card" style="left:593px;top:634px;width:299px;height:192px;padding:40px 0 0 46px">
    <div class="level-no">02 LEVEL</div>
    <div class="level-sub" style="margin-top:10px">TEAM LEADER</div>
  </section>

  <section class="abs card" style="left:42px;top:545px;width:255px;height:265px;padding:60px 0 0 22px">
    <div class="level-no">03 LEVEL</div>
    <div class="level-sub" style="margin-top:8px">MINORITY HALO<br>FRANCHISE OWNERSHIP</div>
  </section>

  <figure class="abs portrait" style="left:321px;top:750px;width:249px;height:265px;padding:18px 17px 0">
    <div class="shot" role="img" aria-label="Two team members seated in a dark wood-panelled office" style="height:209px"></div>
    <figcaption class="name">Marcus and Dev</figcaption>
  </figure>
  <figure class="abs portrait" style="left:590px;top:855px;width:157px;height:213px">
    <div class="shot" role="img" aria-label="Portrait of Gordon Malvery in a dark suit" style="height:163px"></div>
    <figcaption class="name">Gordon Malvery</figcaption>
  </figure>
  <figure class="abs portrait" style="left:763px;top:855px;width:151px;height:213px">
    <div class="shot" role="img" aria-label="Portrait of Tomi Adebanjo in a denim shirt outdoors" style="height:166px;background:linear-gradient(160deg,#6f8b5a,#3f5f86)"></div>
    <figcaption class="name">Tomi Adebanjo</figcaption>
  </figure>
  <figure class="abs portrait" style="left:933px;top:855px;width:160px;height:213px">
    <div class="shot" role="img" aria-label="Portrait of Derek Holloway seated in a black coat and hat" style="height:166px;background:linear-gradient(160deg,#d8d8da,#9a9ca0)"></div>
    <figcaption class="name">Derek Holloway</figcaption>
  </figure>

  <div class="abs brand"><span class="brand-mark"></span><span class="brand-name">HALO PRIMEVIEW HOMES GROUP</span></div>

  <p class="abs contact"><b>For more information visit us at</b>www.jobsathalopview.com and request a<br>meeting with our Managing Broker, Mr. Gordon Malvery.</p>
</div>
</body>
</html>
```